Global Nano Technology Surface Protection company needs a new logo and cards

We are a Global company that will apply nanotechnology coatings on surfaces to prevent growth and spread of bacteria, viruses, mold etc. We deal with large corporates, airlines, hospitals and schools so we are after a new modern, simple and clean look that will have great visual impact.
We a company that is focused on prevention and protection.

Company name, Luminary Fabrications Worldwide

Subtext, Hygienic coating solutions

Logo, LFWW or LFW

Target Market(s)

Hospitals, Transport agencies, Airlines, Corporate entities

Industry/Entity Type

Protection

Contact Information for Business Card

Logo, LFWW or LFW
www.lfww.us
Derek Hawtrey
+64213958260
tidyshieldnz@mailbox.example

Logo Text

LFWW

Requirements
Must have
• Simple clean look
Should not have
• Nothing too messy

```html
<!DOCTYPE html>
<html lang="en">
<head>
<meta charset="utf-8">
<title>Luminary Fabrications Worldwide – Business Cards</title>
<link rel="stylesheet" href="https://fonts.googleapis.com/css2?family=Cinzel:wght@400;600&family=Arimo:wght@400&display=swap">
<style>
  :root {
    --navy: #13225f;
    --navy-map: #1d2f74;
    --grey: #7d7d7d;
    --text-grey: #555a63;
    --rule: #9a9a9a;
    --white: #ffffff;
    --bg: #e9eaec;
  }
  * { box-sizing: border-box; margin: 0; padding: 0; }
  html, body { width: 1200px; height: 1015px; overflow: hidden; background: var(--bg); }
  .canvas {
    width: 1200px; height: 1015px;
    display: flex; flex-direction: column; align-items: center; justify-content: center; gap: 60px;
  }
  .card { position: relative; width: 700px; height: 400px; overflow: hidden; box-shadow: 0 8px 24px rgba(0,0,0,.18); }

  /* Front */
  .card--front { background: var(--navy); }
  .world-map {
    position: absolute; left: 40px; top: 40px; width: 620px; height: 320px;
    background: radial-gradient(ellipse at 50% 50%, var(--navy-map) 0%, rgba(29,47,116,0.4) 60%, rgba(19,34,95,0) 80%);
  }
  .brand { position: absolute; display: flex; align-items: center; gap: 18px; }
  .card--front .brand { left: 80px; top: 160px; }
  .brand__square { width: 56px; height: 56px; flex: none; }
  .card--front .brand__square { background: var(--white); }
  .brand__name {
    font-family: "Cinzel", serif; font-weight: 400; font-size: 24px; line-height: 1.2;
    letter-spacing: 0.5px;
  }
  .card--front .brand__name { color: var(--white); }
  .tagline {
    position: absolute; font-family: "Arimo", sans-serif; font-size: 13px; letter-spacing: 0.3px;
  }
  .card--front .tagline { left: 154px; top: 232px; color: rgba(255,255,255,.8); }

  /* Back */
  .card--back { background: var(--white); }
  .card--back .brand { left: 40px; top: 140px; flex-direction: column; gap: 14px; width: 300px; }
  .card--back .brand__square { background: var(--navy); width: 64px; height: 64px; }
  .card--back .brand__name { color: var(--navy); font-size: 19px; text-align: center; }
  .card--back .tagline { left: 40px; width: 300px; top: 272px; text-align: center; color: var(--text-grey); font-size: 12px; }
  .divider { position: absolute; left: 372px; top: 95px; width: 1px; height: 130px; background: var(--rule); }
  .contact { position: absolute; left: 400px; top: 100px; }
  .contact__name {
    font-family: "Cinzel", serif; font-weight: 600; font-size: 24px; color: var(--navy);
    letter-spacing: 1px; margin-bottom: 14px;
  }
  .contact__list { list-style: none; }
  .contact__item {
    display: flex; align-items: center; gap: 10px;
    font-family: "Arimo", sans-serif; font-size: 17px; color: var(--text-grey); line-height: 26px;
  }
  .contact__icon { width: 16px; height: 16px; flex: none; }
  .band-grey { position: absolute; left: 0; bottom: 0; width: 400px; height: 12px; background: var(--grey); }
  .band-navy { position: absolute; left: 400px; right: 0; bottom: 0; height: 30px; background: var(--navy); }
  .band-navy-side { position: absolute; right: 0; top: 170px; width: 14px; bottom: 0; background: var(--navy); }
</style>
</head>
<body>
<main class="canvas">
  <section class="card card--front" aria-label="Business card front">
    <div class="world-map" role="img" aria-label="Dotted world map background"></div>
    <div class="brand">
      <span class="brand__square"></span>
      <span class="brand__name">LUMINARY FABRICATIONS<br>WORLDWIDE</span>
    </div>
    <p class="tagline">Hygienic coating solutions</p>
  </section>

  <section class="card card--back" aria-label="Business card back">
    <div class="brand">
      <span class="brand__square"></span>
      <span class="brand__name">LUMINARY FABRICATIONS<br>WORLDWIDE</span>
    </div>
    <p class="tagline">Hygienic coating solutions</p>
    <span class="divider"></span>
    <div class="contact">
      <h1 class="contact__name">DEREK HAWTREY</h1>
      <ul class="contact__list">
        <li class="contact__item">
          <svg class="contact__icon" viewBox="0 0 16 16" aria-hidden="true"><rect x="1" y="1" width="14" height="14" rx="2" fill="none" stroke="#13225f" stroke-width="1.5"/><path d="M5 4c-1 1 0 4 2 6s5 3 6 2l-1.5-1.5-1.5 1c-1-.5-2.5-2-3-3l1-1.5z" fill="#13225f"/></svg>
          +64213958260
        </li>
        <li class="contact__item">
          <svg class="contact__icon" viewBox="0 0 16 16" aria-hidden="true"><rect x="1" y="3" width="14" height="10" fill="#13225f"/><path d="M1 3l7 6 7-6" fill="none" stroke="#fff" stroke-width="1.2"/></svg>
          tidyshieldnz@mailbox.example
        </li>
        <li class="contact__item">
          <svg class="contact__icon" viewBox="0 0 16 16" aria-hidden="true"><circle cx="8" cy="8" r="7" fill="#13225f"/><path d="M1 8h14M8 1c-3 3-3 11 0 14M8 1c3 3 3 11 0 14" fill="none" stroke="#fff" stroke-width="1"/></svg>
          www.lfww.us
        </li>
      </ul>
    </div>
    <span class="band-navy-side"></span>
    <span class="band-grey"></span>
    <span class="band-navy"></span>
  </section>
</main>
</body>
</html>
```